Integrative Family Medicine Brochure needed

Looking for a very professional, clean, simple, minimalist, bold well designed brochure.
I am reestablishing my practice in a new town and looking for a new look. I am currently in the process of revising my corporate identity. I recently changed the business name to Bright Path Family Medicine.
You can visit the website http://brightpathcare.net/ to get a feel for what I may be looking for. In the brochure I basically want excerpts from my home page, about, services and contact pages.
I have recently used PixelGuild for both logo and business card and have been very happy, as soon as designs start being submitted I will switch to guaranteed payment.
"Bright path" - similar font to "Cambria" and for "Family medicine" is "Trajan Pro"
I have attached several examples of brochures that have caught my eye to get the creative process started, but I am open to any design that conveys natural, life, health, and wellness.
Ideally colors would be muted or cool with emphasis on blues and greens
Feel free to use example stock photos in your design. I have attached the stock photos I have already purchased for the website.
Reason: Still waiting on a few more submissions, now that payment is guaranteed.
Health conscious people of all ages looking for a family medicine doctor
Town

```html
<!DOCTYPE html>
<html lang="en">
<head>
<meta charset="utf-8">
<title>Bright Path Family Medicine – Trifold Brochure</title>
<link rel="stylesheet" href="https://fonts.googleapis.com/css2?family=Cinzel:wght@700&family=Tinos:ital,wght@0,400;0,700;1,400&display=swap">
<style>
:root{
  --stage:#dfe2de;
  --ink:#1d2a33;
  --green-head:#2f7f3a;
  --tab-red:#d8141b;
  --tab-red-dark:#8e0b10;
  --tab-teal:#1aa3a0;
  --tab-teal-dark:#0d6f74;
  --blue-deep:#0e4f97;
  --gold:#f5d11c;
  --white:#ffffff;
  --link-blue:#1b5fb0;
}
*{box-sizing:border-box;margin:0;padding:0}
html,body{width:1200px;height:848px;overflow:hidden}
body{background:var(--stage);font-family:"Tinos",serif;color:var(--ink);position:relative}

.spread{position:absolute;top:196px;width:584px;height:456px;display:grid;grid-template-columns:repeat(3,1fr);box-shadow:0 4px 14px rgba(0,0,0,.22);overflow:hidden}
.spread--outside{left:10px}
.spread--inside{left:606px;background:linear-gradient(180deg,#e6f2f4 0%,var(--white) 35%,var(--white) 80%,#e3f0f3 100%)}

.panel{position:relative;padding:26px 10px 10px;font-size:7.4px;line-height:1.45;text-align:justify;overflow:hidden}
.panel p{margin-bottom:6px}

.tab{display:inline-block;font-weight:700;color:var(--white);font-size:8.5px;padding:3px 18px 3px 10px;border-radius:0 8px 8px 0;position:absolute;left:0;top:8px}
.tab--red{background:linear-gradient(180deg,#f2343a,var(--tab-red) 60%,var(--tab-red-dark));box-shadow:2px 2px 0 rgba(0,0,0,.35)}
.tab--teal{position:relative;left:-10px;top:0;margin:4px 0 6px;background:linear-gradient(180deg,#4cc6c0,var(--tab-teal) 55%,var(--tab-teal-dark))}
.tab--teal::after{content:"";position:absolute;left:100%;top:50%;width:120px;height:1px;background:var(--tab-teal)}

.panel--about{padding-top:30px;font-size:7.8px;line-height:1.55;background:linear-gradient(165deg,#dcefe6 0%,#f1f7f4 30%,#cfe6ee 70%,#4f9ccd 100%)}
.panel--about p{margin-bottom:12px}
.about-heading{font-size:11.5px;line-height:1.18;font-weight:700;color:var(--green-head);text-align:center;margin:2px 0 12px}
.panel--philosophy{padding-top:30px;font-size:7.8px;line-height:1.55;background:linear-gradient(170deg,#1f73b4 0%,#1e8fb0 35%,#2aa27e 60%,#1c78b6 85%,var(--blue-deep) 100%);color:var(--white)}
.panel--philosophy p{margin-bottom:10px}
.panel--philosophy .narrow{width:60%}
.doctor-photo{position:absolute;right:8px;bottom:0;width:76px;height:120px;border-radius:38px 38px 0 0;background:linear-gradient(180deg,#c9d6dc,#7d8f99 60%,#3f5563)}

.panel--cover{padding:0;background:linear-gradient(180deg,#177fb4 0%,#22a0a4 28%,#56b64b 48%,#3ea27d 64%,#1d6db2 84%,var(--blue-deep) 100%);color:var(--white);text-align:center}
.cover-art{position:absolute;left:0;top:0;width:100%;height:150px}
.cover-photo{position:absolute;left:60px;top:-30px;width:160px;height:160px;border-radius:50%;background:radial-gradient(circle at 50% 55%,#4f9a2d 0%,#7a5a3a 30%,#e6c7b1 55%,#2f9fc4 80%)}
.headline{position:absolute;left:0;right:0;top:168px;font-family:"Cinzel",serif;font-weight:700;color:var(--gold);text-shadow:1px 1px 0 #6b5a05,2px 2px 3px rgba(0,0,0,.35);line-height:1.05;text-align:left;padding-left:22px}
.headline span{display:block}
.headline .l1{font-size:25px}
.headline .l2{font-size:19px;padding-left:20px}
.headline .l3{font-size:19px;padding-left:42px}
.headline .l4{font-size:23px}
.brand{position:absolute;left:0;right:0;top:318px;display:flex;align-items:center;justify-content:center;gap:6px;font-weight:700;font-size:13px;color:var(--white)}
.brand-dot{width:10px;height:10px;border-radius:50%;background:var(--white)}
.contact{position:absolute;left:0;right:0;top:362px;font-size:6.8px;font-weight:700;line-height:1.45}

.panel--services{padding-top:14px}
.photo{border-radius:6px}
.photo--herbs{float:left;width:58px;height:50px;margin:0 6px 2px 0;background:linear-gradient(160deg,#c9a25e,#7f9b3c 55%,#5b3d22)}
.photo--massage{float:left;width:62px;height:58px;margin:4px 6px 0 0;border-radius:50%;background:linear-gradient(160deg,#f2d4bf,#d7a483)}
.photo--veg{float:right;width:76px;height:46px;margin:0 0 3px 6px;background:linear-gradient(160deg,#8fbf4a,#e1633b 55%,#f2e6c2)}
.photo--needles{float:right;width:70px;height:46px;margin:0 0 3px 6px;background:linear-gradient(160deg,#e9d0bf,#c69c82)}
.photo--spine{float:right;width:38px;height:96px;margin:0 0 3px 6px;background:linear-gradient(180deg,#8d7ed6,#3e58c2 55%,#e2e6f2)}
.photo--sneeze{float:right;width:52px;height:88px;margin:4px 0 0 6px;background:linear-gradient(180deg,#c68a52,#f2dcc6 45%,#f3e43b)}
.modality-list{list-style:none;font-weight:700;color:var(--link-blue);font-size:7.2px;line-height:1.4;margin:4px 0 8px;text-align:left}
.labs{background:linear-gradient(180deg,#2bb3ad,var(--tab-teal-dark));color:var(--white);padding:6px 8px;border-radius:2px;margin-top:4px}
.labs-title{font-weight:700;color:var(--gold);font-size:12px;margin-right:3px}
.org{color:var(--link-blue)}
</style>
</head>
<body>

<section class="spread spread--outside" aria-label="Brochure outside">
  <article class="panel panel--about">
    <span class="tab tab--red">About Us</span>
    <h2 class="about-heading">Restoring your Health Naturally with Nutrition, Manipulation, Acupuncture, and Integrative Medicine</h2>
    <p>As an integrative medical practice, we provide innovative, quality family health care by uniquely combining both conventional and alternative medicine. Our aim is to treat the whole patient, not just the symptoms. This best of both worlds approach gives patients more options in managing their concerns while addressing the underlying causes of their illness.</p>
    <p>In our practice, we believe prevention is the key to lifelong health and wellness. We are committed to helping you get well, stay well and live well, and to inspire every patient to follow a path leading to a healthy life.</p>
    <p>At the heart of this practice is the partnership between doctor and patient. Our staff is dedicated to providing compassionate care to patients of all ages, taking time to listen and educate while giving you a positive and satisfying experience.</p>
  </article>

  <article class="panel panel--philosophy">
    <span class="tab tab--red">Philosophy</span>
    <p>My primary purpose is to get people well, and the way I feel this is best done is within the framework of integrative family medicine. I believe medicine is much more than just dispensing pills. Each patient is a member of a family, and I treat them as I would treat my own. Modern lifestyles have brought a rise in chronic illness, and much of what we suffer from is self inflicted by stress, poor diet and lack of rest. Our health is shaped by what we do each day.</p>
    <p class="narrow">Some people come to the doctor looking for the magic pill, but lasting health grows from good food, exercise, sleep and care. Through nutrition, acupuncture, homeopathy and manipulation, it is possible to produce real results, but it still depends on you doing your part.</p>
    <div class="doctor-photo" role="img" aria-label="Portrait photo of the doctor"></div>
  </article>

  <article class="panel panel--cover">
    <svg class="cover-art" viewBox="0 0 195 150" aria-hidden="true">
      <circle cx="140" cy="40" r="110" fill="#1680a8" opacity=".55"/>
      <circle cx="140" cy="40" r="96" fill="none" stroke="#e8f6f8" stroke-width="2.2" stroke-dasharray="0.1 6" stroke-linecap="round"/>
    </svg>
    <div class="cover-photo" role="img" aria-label="Photo of cupped hands holding soil with a green seedling"></div>
    <h1 class="headline"><span class="l1">Helping</span><span class="l2">You Walk</span><span class="l3">a Truly</span><span class="l4">Bright Path</span></h1>
    <div class="brand"><span class="brand-dot"></span>Bright Path Family Medicine</div>
    <div class="contact">
      4180 Meadowridge Road, Townsville Texas 79000<br>
      Telephone: (555) 201-4400<br>
      FAX: (555) 201-4401<br>
      http://brightpathcare.net/
    </div>
  </article>
</section>

<section class="spread spread--inside" aria-label="Brochure inside">
  <article class="panel panel--services">
    <h3 class="tab tab--teal">Family Medicine</h3>
    <p>In addition to what you would expect from any family doctor, Dr. Harlan utilizes many different modalities in his attempt to improve your quality of health, whether it is pharmaceutical or nutraceutical.</p>
    <div class="photo photo--herbs" role="img" aria-label="Photo of herbs and a mortar with pestle"></div>
    <p>Routine primary care is provided for newborns to adults. We do everything that a primary care practice does, plus we deliver it in an integrative way. This includes routine physicals, gynecological care, sick visits and chronic disease management. A network of specialists and other providers are available, which supports an integrative approach.</p>
    <h3 class="tab tab--teal">Manipulation</h3>
    <p>Dr. Harlan has been trained as an Osteopathic Physician and, as such, has been trained in manual manipulation. He has learned from many skilled teachers over the years and continues to attend courses and conferences regarding manipulation.</p>
    <div class="photo photo--massage" role="img" aria-label="Photo of hands treating a patient's shoulder"></div>
    <p>He utilizes many different techniques, from cranial treatments to high velocity adjustments.</p>
  </article>

  <article class="panel panel--services">
    <h3 class="tab tab--teal">Nutrition</h3>
    <div class="photo photo--veg" role="img" aria-label="Photo of fresh vegetables"></div>
    <p>Having a Bachelor's degree in Nutritional Science, Dr. Harlan has the conviction that nutrition is one of the keys to optimal health. Since nutrition has an effect on one's body every day, yet it is not traditionally taught in medical schools, many physicians fall short in treatment of many chronic conditions, as most medications are not designed for long-term therapy. The phrase "You are what you eat" is truer than what one might think.</p>
    <h3 class="tab tab--teal">Acupuncture</h3>
    <div class="photo photo--needles" role="img" aria-label="Photo of acupuncture needles in a hand"></div>
    <p>Medical acupuncture provides many types of approaches that are used depending on the individual and their needs, such as pain management, energy balancing, or treating a systemic condition versus local conditions.</p>
    <ul class="modality-list">
      <li>Auricular Acupuncture</li>
      <li>Chinese Scalp Acupuncture</li>
      <li>Energetic Acupuncture</li>
      <li>Five Element Constitutional Acupuncture</li>
      <li>Pain Management</li>
      <li>Percutaneous Nerve Stimulation</li>
    </ul>
    <p class="labs"><span class="labs-title">Labs</span>We offer many alternative laboratory studies. Testing available includes digestive evaluations, food sensitivities, antioxidant and nutritional deficiencies evaluation, hormonal and heavy metal levels, etc. Expanded blood testing can and will be ordered appropriately.</p>
  </article>

  <article class="panel panel--services">
    <h3 class="tab tab--teal">Prolotherapy</h3>
    <div class="photo photo--spine" role="img" aria-label="Illustration of a human spine"></div>
    <p>Dr. Harlan was first introduced to prolotherapy in medical school. After seeing the potential benefits it could offer a patient suffering with pain, he has sought out training in prolotherapy. Dr. Harlan has been doing prolotherapy since 2010. He has been involved with several different medical groups, including the <span class="org">Regional Society of Orthopedic Medicine</span> and the <span class="org">Plains Association of Regenerative Medicine</span>, and spent two weeks abroad in 2013 with the Hemlock Foundation for their yearly prolotherapy medical mission trip and training.</p>
    <h3 class="tab tab--teal">Allergy Testing</h3>
    <div class="photo photo--sneeze" role="img" aria-label="Photo of a woman sneezing into a tissue"></div>
    <p>The goal of our Allergy Program is to eliminate the reaction to airborne allergens that contribute to hay fever, sinusitis, asthma, and allergic rhinitis. Allergy desensitization involves slowly introducing an antigen into your body. The amount of antigen is gradually increased over time, until the body learns to tolerate it. The body stops overreacting and your allergic reactions start to diminish.</p>
  </article>
</section>

</body>
</html>
```